Reliable and clean label for a natural product!

We would like to have a label design for our CBD SOFT GEL CAPSULES . We are a business family and believe in the power of natural healing. In this label we would like to show a reliable, natural and feminine product mainly.

Font styles to use
Serif
Sans Serif

Colors

Designer to choose colors to be used in the design.

```html
<!DOCTYPE html>
<html lang="es">
<head>
<meta charset="utf-8">
<title>Capsulas Aceite de CBD – Label</title>
<link rel="stylesheet" href="https://fonts.googleapis.com/css2?family=Archivo+Narrow:wght@700&family=Arimo:wght@400;700&display=swap">
<style>
  :root {
    --canvas: #d6d5d6;
    --label-green: #7cc34f;
    --label-green-light: #93d066;
    --label-green-dark: #5aa53a;
    --leaf-deep: #2f7f2c;
    --leaf-mid: #4f9f3f;
    --band-dark: #0f3f28;
    --band-yellow: #f2ea3a;
    --title-white: #f4f4f2;
    --title-shadow: #5b5f58;
    --ink-dark: #16261a;
    --accent-yellow: #f4e63a;
    --soft-white: #eef5e8;
  }
  * { margin: 0; padding: 0; box-sizing: border-box; }
  html, body {
    width: 1200px;
    height: 800px;
    overflow: hidden;
    background: var(--canvas);
  }
  .canvas {
    position: relative;
    width: 1200px;
    height: 800px;
  }
  .label {
    position: absolute;
    left: 281px;
    top: 75px;
    width: 638px;
    height: 649px;
    overflow: hidden;
    background: linear-gradient(100deg, var(--label-green-dark) 0%, var(--label-green) 30%, var(--label-green-light) 60%, var(--label-green) 100%);
    font-family: "Arimo", Arial, sans-serif;
  }
  .leaf-illustration {
    position: absolute;
    left: 110px;
    top: 190px;
    width: 430px;
    height: 360px;
    border-radius: 50% 50% 45% 45%;
    background: radial-gradient(ellipse at center, var(--leaf-mid) 0%, var(--leaf-deep) 55%, rgba(47,127,44,0) 72%);
  }
  .product-title {
    position: absolute;
    left: 112px;
    top: 86px;
    font-family: "Archivo Narrow", "Arial Narrow", sans-serif;
    font-weight: 700;
    font-size: 78px;
    line-height: 72px;
    letter-spacing: 0.5px;
    color: var(--title-white);
    text-shadow: -3px 3px 0 var(--title-shadow);
    text-transform: uppercase;
  }
  .product-type {
    position: absolute;
    left: 105px;
    top: 340px;
    width: 478px;
    height: 57px;
    background: var(--band-yellow);
    color: var(--ink-dark);
    font-weight: 700;
    font-size: 24px;
    line-height: 57px;
    padding-left: 28px;
    letter-spacing: -0.3px;
  }
  .product-specs {
    position: absolute;
    left: 138px;
    top: 440px;
    font-size: 23px;
    line-height: 30px;
    color: var(--soft-white);
    letter-spacing: -0.3px;
  }
  .product-count {
    position: absolute;
    right: 50px;
    top: 500px;
    text-align: center;
    font-weight: 700;
    color: var(--accent-yellow);
  }
  .product-count .count-number {
    display: block;
    font-family: "Archivo Narrow", "Arial Narrow", sans-serif;
    font-size: 72px;
    line-height: 62px;
  }
  .product-count .count-unit {
    display: block;
    font-size: 18px;
    line-height: 20px;
    color: var(--soft-white);
  }
  .product-category {
    position: absolute;
    left: 36px;
    top: 200px;
    height: 300px;
    writing-mode: vertical-rl;
    transform: rotate(180deg);
    text-align: center;
    font-size: 22px;
    color: var(--accent-yellow);
    letter-spacing: 0.2px;
  }
  .label-base {
    position: absolute;
    left: 0;
    bottom: 0;
    width: 100%;
    height: 40px;
    background: var(--band-dark);
  }
</style>
</head>
<body>
  <main class="canvas">
    <section class="label">
      <div class="leaf-illustration" role="img" aria-label="Illustration of a large green hemp leaf behind the title"></div>
      <h1 class="product-title">Capsulas<br>Aceite de<br>CBD</h1>
      <p class="product-type">HEMP OIL EXTRACT CAPSULES</p>
      <p class="product-specs">Full Spectrum<br>25 mg CBD per capsule</p>
      <p class="product-count"><span class="count-number">30</span><span class="count-unit">Capsules</span></p>
      <p class="product-category">Restorative Supplement</p>
      <div class="label-base"></div>
    </section>
  </main>
</body>
</html>
```